Stonebrook 720 Real Estate Investment Company

We need a business card designed for a real estate investment company named Stonebrook 720. We want to use red#f04a50, orange #f37122 and yellow #fbee3e as the color scheme. The logo colors will need to be modified from the current blue palette. I've attach VitaPathway logo example that captures the color scheme we're going for for Stonebrook 720. Looking for clean Sans Serif fonts.
Contact Information for Business Card
Daniel Furlow
Managing Partner
48317 Whitfield Lane, Suite 510
Tampa, FL 33718
813-555-4870 Mobile
dfurlow@stonebrook720.example
www.stonebrook720.example
Requirements
Must have
- Looking for creative responses.
Nice to have
- Must hit color palette... orange, red, yellow

```html
<!DOCTYPE html>
<html lang="en">
<head>
<meta charset="utf-8">
<title>Stonebrook 720 – Business Card</title>
<link href="https://fonts.googleapis.com/css2?family=Roboto+Condensed:wght@400;700&display=swap" rel="stylesheet">
<style>
  :root {
    --bg: #e4e4e6;
    --card-white: #f7f7f7;
    --red: #e0322c;
    --orange: #e2701f;
    --orange-deep: #d8561f;
    --yellow: #e9b01a;
    --ink: #2a2a2a;
    --white: #ffffff;
  }
  html, body {
    margin: 0;
    padding: 0;
    width: 1200px;
    height: 726px;
    overflow: hidden;
    background: var(--bg);
    font-family: "Roboto Condensed", Arial, sans-serif;
  }
  .stage {
    position: relative;
    width: 1200px;
    height: 726px;
  }
  .card {
    position: absolute;
    top: 208px;
    width: 540px;
    height: 309px;
    border-radius: 4px;
    overflow: hidden;
    box-shadow: 0 6px 18px rgba(0,0,0,0.15);
  }
  /* Front */
  .card--front {
    left: 40px;
    background: linear-gradient(30deg, var(--orange) 0%, var(--orange-deep) 55%, var(--red) 100%);
    display: flex;
    flex-direction: column;
    align-items: center;
    justify-content: center;
  }
  .front-name {
    color: var(--white);
    font-weight: 700;
    font-size: 58px;
    letter-spacing: 0.5px;
    line-height: 1;
  }
  .front-url {
    margin-top: 8px;
    color: var(--ink);
    font-size: 15px;
    letter-spacing: 3px;
  }
  /* Back */
  .card--back {
    left: 620px;
    background: var(--card-white);
  }
  .band {
    position: absolute;
    inset: 0;
  }
  .back-name {
    position: absolute;
    left: 30px;
    top: 78px;
    color: var(--orange);
    font-weight: 700;
    font-size: 32px;
    line-height: 1;
  }
  .contact {
    position: absolute;
    left: 30px;
    top: 150px;
    color: var(--white);
  }
  .contact__name {
    font-weight: 700;
    font-size: 21px;
    margin: 0;
  }
  .contact__title {
    font-size: 13px;
    margin: 2px 0 12px;
  }
  .contact__list {
    list-style: none;
    margin: 0;
    padding: 0;
    font-size: 13px;
  }
  .contact__list li {
    display: flex;
    align-items: center;
    gap: 10px;
    height: 18px;
  }
  .icon {
    width: 12px;
    height: 12px;
    fill: var(--white);
    stroke: var(--white);
  }
  .address {
    position: absolute;
    left: 30px;
    bottom: 18px;
    color: var(--ink);
    font-size: 14px;
  }
</style>
</head>
<body>
<main class="stage">
  <section class="card card--front">
    <div class="front-name">Stonebrook720</div>
    <div class="front-url">www.stonebrook720.example</div>
  </section>

  <section class="card card--back">
    <svg class="band" width="540" height="309" viewBox="0 0 540 309" aria-hidden="true">
      <defs>
        <linearGradient id="bandFill" x1="0" y1="1" x2="1" y2="0">
          <stop offset="0" stop-color="#e0322c"/>
          <stop offset="0.5" stop-color="#e2701f"/>
          <stop offset="1" stop-color="#e9b01a"/>
        </linearGradient>
      </defs>
      <path d="M0 128 L300 128 C330 128 345 112 352 90 L372 20 L410 20 L410 270 L0 270 Z" fill="url(#bandFill)"/>
    </svg>

    <svg class="band" width="540" height="309" viewBox="0 0 540 309" role="img" aria-label="Decorative illustration of falling drops and ripples in red, orange and yellow">
      <defs>
        <linearGradient id="artFill" x1="0" y1="1" x2="1" y2="0">
          <stop offset="0" stop-color="#e0322c"/>
          <stop offset="0.55" stop-color="#e2701f"/>
          <stop offset="1" stop-color="#e9b01a"/>
        </linearGradient>
      </defs>
      <rect x="390" y="20" width="150" height="230" fill="url(#artFill)" opacity="0.85"/>
    </svg>

    <div class="back-name">Stonebrook720</div>

    <div class="contact">
      <p class="contact__name">Daniel Furlow</p>
      <p class="contact__title">Managing Partner</p>
      <ul class="contact__list">
        <li>
          <svg class="icon" viewBox="0 0 12 12"><path d="M2 1 L4.5 1 L5 3.5 L3.8 4.5 C4.5 6 6 7.5 7.5 8.2 L8.5 7 L11 7.5 L11 10 C6 10.5 1.5 6 2 1 Z" stroke="none"/></svg>
          813-555-4870 Mobile
        </li>
        <li>
          <svg class="icon" viewBox="0 0 12 12"><rect x="1" y="2.5" width="10" height="7" fill="none" stroke-width="1.3"/><path d="M1 2.5 L6 6.5 L11 2.5" fill="none" stroke-width="1.3"/></svg>
          dfurlow@stonebrook720.example
        </li>
        <li>
          <svg class="icon" viewBox="0 0 12 12"><circle cx="6" cy="6" r="5" fill="none" stroke-width="1.2"/><ellipse cx="6" cy="6" rx="2.2" ry="5" fill="none" stroke-width="1"/><path d="M1 6 H11" stroke-width="1"/></svg>
          www.stonebrook720.example
        </li>
      </ul>
    </div>

    <div class="address">48317 Whitfield Lane, Suite 510 Tampa, FL 33718</div>
  </section>
</main>
</body>
</html>
```